Design some Business Cards for The Larkwell

I require a design for business cards that is based off my current design theme.

I want them to be fun but professional.

Must use Timber/yellow background/cherry logo as attached and on website

The website is www.thelarkwell.com.au and the files needed are attached.

The text requires the following fields:

Derek Hollis
Managing Director
Phone - XXXX XXX XXX
Email - derek@thelarkwell.com.au
www.thelarkwell.com.au

Full Bleed Size (starting document size)
90 x 52 mm
1062 x 615 pixels
* Finished artwork should use the full bleed dimensions

Document Trim Size (final size after being cut)
87 x 49 mm
1028 x 579 pixels
* Please be sure to keep all text within the safe margin.

Resolution
300 DPI

All designs must be provided in .PSD upon completion.

```html
<!DOCTYPE html>
<html lang="en">
<head>
<meta charset="utf-8">
<title>The Larkwell — Business Cards</title>
<link rel="stylesheet" href="https://fonts.googleapis.com/css2?family=Open+Sans:wght@300;400;700&display=swap">
<style>
  :root {
    --stage: #2b2b2b;
    --yellow: #f4e31c;
    --yellow-edge: #e3cf0e;
    --yellow-shade: #cdb808;
    --wood-dark: #4a3626;
    --wood-mid: #6b513b;
    --wood-light: #7d604a;
    --accent-red: #d9293f;
    --ink: #161616;
    --rivet: #b9bcc0;
    --rivet-ring: #7e8287;
    --cream: #f4ead2;
    --white: #ffffff;
  }
  * { box-sizing: border-box; margin: 0; padding: 0; }
  html, body { width: 1200px; height: 899px; overflow: hidden; }
  body {
    background: var(--stage);
    font-family: "Open Sans", Arial, sans-serif;
    position: relative;
  }
  .card {
    position: absolute;
    left: 250px;
    width: 700px;
    height: 394px;
    background: var(--yellow);
    overflow: hidden;
    box-shadow: 0 10px 24px rgba(0,0,0,.45);
  }
  .card--front { top: 24px; }
  .card--back { top: 458px; }

  .edge-band {
    position: absolute; left: 0; right: 0; height: 16px;
    background: var(--yellow-edge);
  }
  .edge-band--top { top: 0; border-bottom: 2px solid var(--yellow-shade); }
  .edge-band--bottom { bottom: 0; border-top: 2px solid var(--yellow-shade); }

  .timber {
    position: absolute;
    background: linear-gradient(90deg, var(--wood-dark) 0%, var(--wood-mid) 35%, var(--wood-light) 60%, var(--wood-mid) 85%, var(--wood-dark) 100%);
    box-shadow: inset 0 0 14px rgba(0,0,0,.45);
  }
  .card--front .timber--left { left: 0; top: 46px; width: 228px; height: 212px; }
  .card--front .timber--right { left: 462px; top: 150px; width: 238px; height: 200px; }
  .card--back .timber--main {
    left: 300px; top: 30px; width: 400px; height: 328px;
    clip-path: polygon(0 0, 100% 0, 100% 100%, 0 100%, 0 30%, 4% 26%, 0 22%);
  }

  .rivet {
    position: absolute; width: 12px; height: 12px; border-radius: 50%;
    background: radial-gradient(circle at 40% 40%, var(--white), var(--rivet) 55%, var(--rivet-ring));
    box-shadow: 0 1px 2px rgba(0,0,0,.4);
  }

  .web-ribbon {
    position: absolute; left: 56px; top: 38px; width: 206px; height: 26px;
    background: var(--accent-red);
    color: var(--white);
    font-size: 13px; line-height: 26px; padding-left: 14px;
    white-space: nowrap;
    clip-path: polygon(0 0, 100% 0, 94% 50%, 100% 100%, 0 100%);
  }
  .web-ribbon strong { font-weight: 700; }

  .brand {
    position: absolute;
    display: flex; align-items: center; gap: 10px;
    color: var(--ink);
    font-weight: 700;
    font-size: 26px;
    line-height: 1;
    white-space: nowrap;
  }
  .brand__mark {
    width: 30px; height: 30px; border-radius: 50%;
    background: var(--accent-red); flex: none;
  }
  .card--front .brand { left: 244px; top: 186px; }
  .card--back .brand { left: 44px; top: 92px; }

  .person { position: absolute; left: 338px; top: 106px; }
  .person__name { color: var(--yellow); font-size: 25px; font-weight: 400; }
  .person__role { color: var(--cream); font-size: 14px; font-weight: 300; margin-top: 2px; }

  .contact {
    position: absolute; left: 338px; top: 218px;
    list-style: none; color: var(--cream); font-size: 16px; font-weight: 300;
  }
  .contact li { display: flex; align-items: center; gap: 10px; height: 24px; }
  .contact__icon { width: 16px; height: 16px; flex: none; }
  .contact__text strong { font-weight: 700; }
</style>
</head>
<body>

<section class="card card--front" aria-label="Card front">
  <div class="edge-band edge-band--top"></div>
  <div class="edge-band edge-band--bottom"></div>
  <div class="timber timber--left" role="img" aria-label="Dark timber plank texture"></div>
  <div class="timber timber--right" role="img" aria-label="Dark timber plank texture"></div>
  <div class="web-ribbon">www.<strong>thelarkwell</strong>.com.au</div>
  <div class="brand">
    <span class="brand__name">The Larkwell</span>
    <span class="brand__mark"></span>
  </div>
  <span class="rivet" style="left:236px;top:70px"></span>
  <span class="rivet" style="left:236px;top:300px"></span>
  <span class="rivet" style="left:446px;top:118px"></span>
  <span class="rivet" style="left:446px;top:330px"></span>
</section>

<section class="card card--back" aria-label="Card back">
  <div class="edge-band edge-band--top"></div>
  <div class="edge-band edge-band--bottom"></div>
  <div class="timber timber--main" role="img" aria-label="Dark timber plank texture"></div>
  <div class="brand">
    <span class="brand__name">The Larkwell</span>
    <span class="brand__mark"></span>
  </div>
  <div class="person">
    <div class="person__name">Derek Hollis</div>
    <div class="person__role">Managing Director</div>
  </div>
  <ul class="contact">
    <li>
      <svg class="contact__icon" viewBox="0 0 16 16"><rect width="16" height="16" rx="2" fill="var(--accent-red)"/><path d="M5 3.5l2 2-1 1.2c.6 1.3 1.7 2.4 3 3l1.2-1 2 2-1.4 1.6C7.6 12 4 8.4 3.7 5.2z" fill="var(--white)"/></svg>
      <span class="contact__text">+000-000-4821</span>
    </li>
    <li>
      <svg class="contact__icon" viewBox="0 0 16 16"><rect width="16" height="16" rx="2" fill="var(--accent-red)"/><rect x="3" y="4.5" width="10" height="7" fill="none" stroke="var(--white)" stroke-width="1.2"/><path d="M3 4.5l5 4 5-4" fill="none" stroke="var(--white)" stroke-width="1.2"/></svg>
      <span class="contact__text">derek@thelarkwell.com.au</span>
    </li>
    <li>
      <svg class="contact__icon" viewBox="0 0 16 16"><rect width="16" height="16" rx="2" fill="var(--accent-red)"/><circle cx="8" cy="8" r="4.5" fill="none" stroke="var(--white)" stroke-width="1.2"/><path d="M3.5 8h9M8 3.5c-2 2.5-2 6.5 0 9M8 3.5c2 2.5 2 6.5 0 9" fill="none" stroke="var(--white)" stroke-width="1"/></svg>
      <span class="contact__text">www.<strong>thelarkwell</strong>.com.au</span>
    </li>
  </ul>
  <span class="rivet" style="left:56px;top:22px"></span>
  <span class="rivet" style="left:56px;top:362px"></span>
  <span class="rivet" style="left:276px;top:22px"></span>
  <span class="rivet" style="left:276px;top:362px"></span>
</section>

</body>
</html>
```